Powerful crowd generating flyer to be built

What we are looking for is a cleverly worded flyer with a sophisticated graphic design. Our objective is to generate inquires and represent our brand.

Who we are: We a boutique gym in the Eastern Suburbs of Sydney. Up market, designer space, superior customer service and the very latest equipment. Our gym is like no other, innovative equipment from rock climbing wall, tensiqo frames, KVL, sprint track, innovative classes never seen before in Sydney. Please refer to "Keel Motion" (www.keelmotion.com.au) "GX yard" (www.gxyard.com.au) and "Vrelo" (www.vrelo.com.au) for like for like gyms to gain a feeling on who we are.. We are: www.marrowindfitnessclub.com.au (Please refer to this website for further photos)

Some of the services which need to be mentioned
1) Free Creche
2) Sydney most innovative classes
3) Sydney's best personal trainers
4) Free Parking

The OFFER: No Joining Fee, one month free membership (T&C apply) Limited space on offer, and only valid until 30.11.13

We are a cool looking gym, so we need a flyer which is slightly edgy, sophisticated and sleek.

Target Market(s)

60:40 Female to Male.
20 to 45 years old
Professionals and Mothers
Up market, wealthy, discerning

Industry/Entity Type

Boutique

Requirements
Must have
• The Flyer must be double sided, use a combination ofcthe photos attached,
Should not have
• cheese, generic, classic gym looking flyer

```html
<!DOCTYPE html>
<html lang="en">
<head>
<meta charset="utf-8">
<title>Marrowind Fitness Club – Flyer</title>
<link href="https://fonts.googleapis.com/css2?family=Ubuntu:wght@300;400;500;700&display=swap" rel="stylesheet">
<style>
  :root {
    --yellow: #f4ef1c;
    --mist: #e6e8e8;
    --slate: #4a4d4e;
    --ink: #3d3d3d;
    --band: #b7bac6;
    --ring: #555859;
    --sans: "Ubuntu", "Helvetica Neue", Arial, sans-serif;
  }
  * { box-sizing: border-box; margin: 0; padding: 0; }
  html, body { width: 1200px; height: 1200px; overflow: hidden; background: #ffffff; }
  body { position: relative; font-family: var(--sans); color: var(--ink); }

  .flyer { position: absolute; top: 53px; width: 483px; height: 967px; overflow: hidden; }
  .flyer--front { left: 79px; }
  .flyer--back { left: 642px; }
  .flyer__art { position: absolute; inset: 0; width: 100%; height: 100%; display: block; }

  .side-label {
    position: absolute; top: 1070px; width: 400px; text-align: center;
    font-weight: 500; font-size: 54px; color: #111; letter-spacing: 1px;
  }
  .side-label--front { left: 100px; }
  .side-label--back { left: 700px; }

  /* Front */
  .brand { position: absolute; left: 0; width: 410px; text-align: center; }
  .brand__name { top: 190px; font-weight: 300; font-size: 42px; letter-spacing: 3px; color: #555; }
  .brand__sub { top: 252px; font-weight: 300; font-size: 16px; letter-spacing: 4px; color: #555; }

  .perks { position: absolute; right: 121px; top: 0; width: 360px; list-style: none; }
  .perk { position: absolute; right: 0; white-space: nowrap; font-size: 20px; color: var(--ink); }

  .offer {
    position: absolute; left: 0; width: 470px; top: 790px;
    text-align: center; font-size: 14px; line-height: 19.5px; color: #2e2e2e;
  }
  .front-url {
    position: absolute; left: 0; width: 478px; top: 910px;
    text-align: center; font-size: 25px; color: var(--ink);
  }

  /* Back */
  .trainers-title {
    position: absolute; right: 41px; top: 38px; text-align: right;
    font-weight: 500; font-size: 52px; line-height: 57px; color: #4f4f4f;
    text-shadow: 1px 1px 0 #ffffff, 3px 3px 4px rgba(0,0,0,.35);
  }
  .services-heading { position: absolute; left: 38px; top: 627px; font-size: 20px; color: #3f3f3f; }
  .service { position: absolute; font-size: 16px; line-height: 20px; color: var(--ink); white-space: nowrap; }
  .service--l { left: 29px; }
  .service--c { left: 172px; width: 140px; text-align: center; }
  .service--c.service--wide { left: 152px; width: 180px; }
  .service--r { right: 33px; text-align: right; }

  .row-1 { top: 685px; }
  .row-2 { top: 710px; }
  .row-3 { top: 734px; }
  .row-4 { top: 775px; }
  .row-5 { top: 812px; }
  .row-6 { top: 848px; }

  .contact { position: absolute; left: 0; width: 483px; color: var(--yellow); font-size: 19px; line-height: 24px; }
  .contact--tel { top: 893px; text-align: center; }
  .contact--address { top: 925px; left: 46px; width: auto; }
  .contact__dots { letter-spacing: 0.5px; }
</style>
</head>
<body>

<section class="flyer flyer--front">
  <svg class="flyer__art" viewBox="0 0 402 806" preserveAspectRatio="none">
    <rect width="402" height="806" fill="var(--yellow)"/>
    <path d="M0,430 C130,420 260,300 402,175 L402,205 C260,320 130,445 0,455 Z" fill="#c9cbcb"/>
    <path d="M0,478 C140,470 260,360 402,240 L402,730 L0,730 Z" fill="var(--mist)"/>
    <path d="M0,478 C140,470 260,360 402,240" fill="none" stroke="#6a6d6e" stroke-width="3"/>
    <rect x="0" y="730" width="402" height="8" fill="var(--slate)"/>
    <rect x="0" y="738" width="402" height="68" fill="var(--yellow)"/>

    <defs>
      <linearGradient id="photoA" x1="0" y1="0" x2="1" y2="1">
        <stop offset="0" stop-color="#8a6a55"/><stop offset="1" stop-color="#5b7a8a"/>
      </linearGradient>
      <linearGradient id="photoB" x1="0" y1="0" x2="1" y2="1">
        <stop offset="0" stop-color="#c9d3d6"/><stop offset="1" stop-color="#7d8f74"/>
      </linearGradient>
      <linearGradient id="photoC" x1="0" y1="0" x2="0" y2="1">
        <stop offset="0" stop-color="#7a5a46"/><stop offset=".6" stop-color="#6f8fa0"/><stop offset="1" stop-color="#c0583a"/>
      </linearGradient>
    </defs>
    <circle cx="279" cy="286" r="38" fill="url(#photoA)" stroke="var(--ring)" stroke-width="3" role="img" aria-label="Photo: climbing wall studio with two members stretching on mats"/>
    <circle cx="207" cy="341" r="44" fill="url(#photoB)" stroke="var(--ring)" stroke-width="3" role="img" aria-label="Photo: bright gym floor with glass roof and plants"/>
    <circle cx="112" cy="406" r="62" fill="url(#photoC)" stroke="var(--ring)" stroke-width="3" role="img" aria-label="Photo: indoor training hall with sprint track and rig"/>

    <g class="tickbox" fill="none" stroke="#3d3d3d">
      <rect x="321" y="432" width="38" height="24" stroke-width="2.5"/>
      <path d="M327,440 L337,452 L371,425" stroke-width="5" stroke-linejoin="round"/>
      <rect x="321" y="485" width="38" height="24" stroke-width="2.5"/>
      <path d="M327,493 L337,505 L371,478" stroke-width="5" stroke-linejoin="round"/>
      <rect x="321" y="540" width="38" height="24" stroke-width="2.5"/>
      <path d="M327,548 L337,560 L371,533" stroke-width="5" stroke-linejoin="round"/>
      <rect x="321" y="595" width="38" height="24" stroke-width="2.5"/>
      <path d="M327,603 L337,615 L371,588" stroke-width="5" stroke-linejoin="round"/>
    </g>
  </svg>

  <div class="brand brand__name">MARROWIND</div>
  <div class="brand brand__sub">FITNESS CLUB</div>

  <ul class="perks">
    <li class="perk" style="top:520px">Free Creche</li>
    <li class="perk" style="top:583px">Free Parking</li>
    <li class="perk" style="top:649px">Sydney most innovative classes</li>
    <li class="perk" style="top:715px">Sydney's best personal trainers</li>
  </ul>

  <p class="offer">No Joining Fee,<br>one month free membership (T&amp;C apply)<br>Limited space on offer, and only valid until 30.11.13</p>
  <p class="front-url">www.marrowindfitnessclub.com.au</p>
</section>

<section class="flyer flyer--back">
  <svg class="flyer__art" viewBox="0 0 402 806" preserveAspectRatio="none">
    <defs>
      <linearGradient id="trainerA" x1="0" y1="0" x2="1" y2="1">
        <stop offset="0" stop-color="#3c4a4e"/><stop offset="1" stop-color="#b98a6a"/>
      </linearGradient>
      <linearGradient id="trainerB" x1="0" y1="0" x2="0" y2="1">
        <stop offset="0" stop-color="#5a4a40"/><stop offset="1" stop-color="#a97a5c"/>
      </linearGradient>
      <linearGradient id="trainerC" x1="0" y1="0" x2="1" y2="1">
        <stop offset="0" stop-color="#d9d9d9"/><stop offset="1" stop-color="#6e6e6e"/>
      </linearGradient>
    </defs>
    <rect width="402" height="806" fill="var(--yellow)"/>
    <path d="M0,168 C120,205 260,340 402,420 L402,482 C260,425 120,335 0,268 Z" fill="var(--mist)"/>
    <path d="M0,268 C120,335 260,425 402,482" fill="none" stroke="#555" stroke-width="5"/>
    <rect x="0" y="514" width="402" height="34" fill="var(--band)"/>
    <rect x="0" y="548" width="402" height="183" fill="var(--mist)"/>
    <rect x="0" y="731" width="402" height="7" fill="var(--yellow)"/>
    <rect x="0" y="738" width="402" height="68" fill="var(--slate)"/>

    <circle cx="103" cy="201" r="66" fill="url(#trainerA)" stroke="var(--ring)" stroke-width="3" role="img" aria-label="Photo: personal trainer portrait by a climbing net"/>
    <circle cx="203" cy="276" r="62" fill="url(#trainerB)" stroke="var(--ring)" stroke-width="3" role="img" aria-label="Photo: trainer crouched in a focused stance"/>
    <circle cx="305" cy="361" r="60" fill="url(#trainerC)" stroke="var(--ring)" stroke-width="3" role="img" aria-label="Photo: black and white barbell squat"/>
    <circle cx="93" cy="388" r="64" fill="url(#trainerB)" stroke="var(--ring)" stroke-width="3" role="img" aria-label="Photo: boxing pad session with trainer"/>
    <circle cx="190" cy="443" r="58" fill="url(#trainerA)" stroke="var(--ring)" stroke-width="3" role="img" aria-label="Photo: trainer using gymnastic rings"/>
    <circle cx="291" cy="503" r="62" fill="url(#trainerC)" stroke="var(--ring)" stroke-width="3" role="img" aria-label="Photo: trainer with medicine ball"/>
  </svg>

  <h2 class="trainers-title">Meet Our<br>Personal<br>Trainers</h2>

  <p class="services-heading">Our sevices include:</p>

  <span class="service service--l row-1">Yoga</span>
  <span class="service service--c row-1">Boxing</span>
  <span class="service service--r row-1" style="top:688px">Pilates</span>
  <span class="service service--l row-2">tensiqo</span>
  <span class="service service--c row-2">Aerobics</span>
  <span class="service service--r row-2">Bounzo</span>
  <span class="service service--l row-3">Kettlebells</span>
  <span class="service service--c service--wide row-3">Weight Training</span>
  <span class="service service--r row-3">Circuit Training</span>

  <span class="service service--l row-4">Group Fitness for Women</span>
  <span class="service service--r row-4">Losing Weight &amp; Toning</span>
  <span class="service service--l row-5">Build Muscle &amp; Definition</span>
  <span class="service service--r row-5" style="top:810px">Gym Creche/Childcare</span>
  <span class="service service--l row-6">Post Pregnancy Gym Classes</span>
  <span class="service service--r row-6">Bootcamping</span>

  <p class="contact contact--tel">Tel: (02) 9000 4821</p>
  <p class="contact contact--address">Address: <span class="contact__dots">.......................................................</span></p>
</section>

<div class="side-label side-label--front">FRONT</div>
<div class="side-label side-label--back">BACK</div>

</body>
</html>
```